Sphynx Cat Breeder

Hi.
I have just got a logo through Pixel Harbor, and now I need a website.
I am home based Sphynx cat breeder (Plumwick Sphynx)
I want to be able to show my breedings cats and kittens available for sale on my website.

Target Market(s)

Buyers of pet kittens in New Zealand, plus potentially buyers of kittens for breeding for overseas breeders

Requirements
Must have
• Home page
About Us
My breeding Cats
Kittens
Caring for a Sphynx
Links
Contact (contact details plus a link to email)
I need to be able to upload photos as kittens come and go.
Nice to have
• A web counter, visible only to me, preferably showing which country they are from

```html
<!DOCTYPE html>
<html lang="en">
<head>
<meta charset="utf-8">
<title>Plumwick Sphynx</title>
<link rel="stylesheet" href="https://fonts.googleapis.com/css2?family=Roboto+Condensed:wght@700&family=PT+Sans:wght@400;700&family=Arimo:wght@400&display=swap">
<style>
:root{
  --cyan:#00b6d3;
  --cyan-dark:#0a8aa0;
  --ink:#444;
  --text:#5a5a5a;
  --nav-dark:#151515;
  --page-bg:#f1f1f1;
  --white:#fff;
}
*{box-sizing:border-box;margin:0;padding:0}
html,body{width:1172px;height:1200px;overflow:hidden}
body{background:var(--page-bg);font-family:"Arimo",Arial,sans-serif;position:relative}
.page{position:absolute;left:77px;top:0;width:996px;height:1200px;background:var(--white);border-top:4px solid var(--cyan);box-shadow:0 0 8px rgba(0,0,0,.12)}
.site-header{position:relative;height:171px;background:linear-gradient(#fff 0%,#f7f7f7 50%,#ededed 100%)}
.brand{position:absolute;left:30px;top:22px;display:flex;flex-direction:column;align-items:center;gap:12px}
.brand-mark{width:112px;height:112px;border:9px solid #1c1c1c;border-radius:50%}
.brand-name{font-family:"PT Sans",sans-serif;font-weight:700;font-size:17px;color:#1c1c1c}
.main-nav{position:absolute;left:243px;top:111px;width:750px;height:40px;background:linear-gradient(#3a3a3a,#0d0d0d);border-radius:12px;display:flex;align-items:center;padding-left:21px}
.main-nav a{font-family:"PT Sans",sans-serif;font-size:14px;color:#fff;text-decoration:none;height:40px;display:flex;align-items:center;justify-content:center;border-right:1px solid #333}
.main-nav a:last-child{border-right:none}
.main-nav a.active{height:57px;margin-top:-17px;padding-top:17px;background:linear-gradient(#1ccfe6,#00a9c4);border-radius:0 0 6px 6px}
.welcome{text-align:center;padding-top:10px}
.welcome h1{font-family:"Roboto Condensed",sans-serif;font-size:30px;color:var(--ink);letter-spacing:.3px}
.welcome h1 span{color:var(--cyan)}
.welcome p{width:720px;margin:15px auto 0;font-size:12.5px;line-height:20px;color:var(--text)}
.hero{position:absolute;left:8px;top:323px;width:979px;height:384px;border-radius:22px;background:linear-gradient(180deg,#e9e9e9 0%,#f9f9f9 40%,#f3f3f3 80%,#e2e2e2 100%);box-shadow:inset 0 0 14px rgba(0,0,0,.06)}
.hero-copy{position:absolute;left:62px;top:28px;width:395px}
.hero-copy h2{font-family:"Roboto Condensed",sans-serif;font-size:30px;color:var(--cyan);letter-spacing:.5px}
.hero-copy h3{font-family:"Roboto Condensed",sans-serif;font-size:25px;line-height:35px;color:var(--ink);margin-top:3px;letter-spacing:.3px}
.hero-copy p{margin-top:25px;width:388px;font-size:12.5px;line-height:20px;color:var(--text);text-align:justify;padding-left:3px}
.cta{position:absolute;left:65px;top:300px;width:166px;height:41px;border-radius:21px;background:linear-gradient(#2cc7e2,#0796b0);box-shadow:0 0 0 2px #fff,0 2px 4px rgba(0,0,0,.25);display:flex;align-items:center;padding-left:15px;font-family:"Roboto Condensed",sans-serif;font-size:21px;color:#fff;text-decoration:none}
.cta svg{position:absolute;right:5px;top:5px}
.hero-photo{position:absolute;left:470px;top:18px;width:440px;height:350px;border-radius:30px;background:radial-gradient(ellipse at 55% 50%,#dcc0c0 0%,#e8d4d2 40%,rgba(245,240,240,0) 75%)}
.arrow{position:absolute;top:172px;width:42px;height:42px}
.arrow.prev{left:7px}
.arrow.next{right:22px}
.section-tab{position:absolute;left:23px;top:732px;width:178px;height:32px;background:linear-gradient(#17c6e0,#00a3bf);clip-path:polygon(0 0,100% 0,93% 100%,0 100%);font-family:"Roboto Condensed",sans-serif;font-size:20px;color:#fff;padding:2px 0 0 13px;letter-spacing:.5px}
.kitten{position:absolute;width:124px;text-align:center}
.kitten-photo{width:120px;height:90px;margin:0 auto;border:1px solid #ddd}
.kitten-photo + .shadow{height:8px;margin:1px auto 0;width:124px;background:radial-gradient(ellipse at 50% 0,rgba(0,0,0,.35),rgba(0,0,0,0) 70%)}
.kitten a{display:inline-block;margin-top:13px;font-family:"PT Sans",sans-serif;font-size:11px;color:#444;text-decoration:none;border-bottom:1px solid #aaa;line-height:13px}
.site-footer{position:absolute;left:0;top:1110px;width:996px;height:90px;background:linear-gradient(#00c6e2 0%,#00b4cf 50%,#0a8aa0 100%);text-align:center;font-family:"PT Sans",sans-serif;font-weight:700;color:#fff}
.footer-nav{display:flex;justify-content:center;gap:0;padding-top:10px;font-size:14px}
.footer-nav a{color:#fff;text-decoration:none}
.footer-nav .sep{margin:0 26px}
.copyright{margin-top:9px;font-size:14px}
</style>
</head>
<body>
<div class="page">
  <header class="site-header">
    <div class="brand">
      <div class="brand-mark"></div>
      <div class="brand-name">Plumwick Sphynx</div>
    </div>
    <nav class="main-nav">
      <a class="active" href="#" style="width:97px">Home</a>
      <a href="#" style="width:108px">About Us</a>
      <a href="#" style="width:160px">My breeding Cats</a>
      <a href="#" style="width:91px">Kittens</a>
      <a href="#" style="width:166px">Caring for a Sphynx</a>
      <a href="#" style="width:106px">Contact Us</a>
    </nav>
  </header>

  <section class="welcome">
    <h1><span>Welcome to</span> Plumwick Sphynx</h1>
    <p>Lorem Ipsum is simply dummy text of the printing and typesetting industry. Lorem Ipsum has been the industry's standard dummy text ever since the 1500s, when an unknown printer took a galley of type and scrambled it to make a type specimen book.Lorem Ipsum is simply dummy text of the printing and typesetting industry. Lorem Ipsum has been the industry's standard dummy text ever since the 1500s, when an unknown printer took a galley of type and scrambled it</p>
  </section>

  <section class="hero">
    <svg class="arrow prev" viewBox="0 0 42 42"><circle cx="21" cy="21" r="20" fill="#0aa7c2" stroke="#fff" stroke-width="2"/><path d="M26 11 L13 21 L26 31 Z" fill="#fff"/></svg>
    <div class="hero-copy">
      <h2>Sphynx cat breeder</h2>
      <h3>Cat and Kittens available for Sale on this websites</h3>
      <p>Lorem Ipsum is simply dummy text of the printing and typesetting industry. Lorem Ipsum has been the industry's standard dummy text ever since the 1500s, when an unknown printer took a galley of type and scrambled it to make a type specimen book. It has survived not only five centuries, but also the leap into electronic typesetting, remaining essentially unchanged.</p>
      <a class="cta" href="#">Click Here
        <svg width="32" height="32" viewBox="0 0 32 32"><circle cx="16" cy="16" r="15" fill="#e9e9e9"/><path d="M10 10 L16 16 L10 22 M16 10 L22 16 L16 22" fill="none" stroke="#7a7a7a" stroke-width="2.5"/></svg>
      </a>
    </div>
    <div class="hero-photo" role="img" aria-label="Photo of two sphynx cats, a kitten sitting and an adult crouching"></div>
    <svg class="arrow next" viewBox="0 0 42 42"><circle cx="21" cy="21" r="20" fill="#0aa7c2" stroke="#fff" stroke-width="2"/><path d="M16 11 L29 21 L16 31 Z" fill="#fff"/></svg>
  </section>

  <h2 class="section-tab">Newest Kittens</h2>

  <div class="kitten" style="left:47px;top:791px"><div class="kitten-photo" role="img" aria-label="Photo of sphynx kittens" style="background:linear-gradient(135deg,#6e5a4e,#9a8a86)"></div><div class="shadow"></div><a href="#">1st: Sphynx cat breeder</a></div>
  <div class="kitten" style="left:193px;top:791px"><div class="kitten-photo" role="img" aria-label="Photo of a spotted sphynx kitten" style="background:linear-gradient(135deg,#3e2f2a,#d9d2cc)"></div><div class="shadow"></div><a href="#">2nd: Sphynx cat</a></div>
  <div class="kitten" style="left:344px;top:791px"><div class="kitten-photo" role="img" aria-label="Photo of a grey sphynx kitten" style="background:linear-gradient(135deg,#8a7b78,#7c7f95)"></div><div class="shadow"></div><a href="#">3rd: Sphynx cat breeder</a></div>
  <div class="kitten" style="left:500px;top:794px"><div class="kitten-photo" role="img" aria-label="Photo of a sphynx kitten lying down" style="background:linear-gradient(180deg,#cfe0ec,#d8c6c2 60%,#f2f2f2)"></div><div class="shadow"></div><a href="#">4th: Sphynx cat</a></div>
  <div class="kitten" style="left:652px;top:791px"><div class="kitten-photo" role="img" aria-label="Photo of a sphynx kitten sitting" style="background:linear-gradient(135deg,#8f8b84,#cfcac4)"></div><div class="shadow"></div><a href="#">2nd: Sphynx cat</a></div>
  <div class="kitten" style="left:808px;top:794px"><div class="kitten-photo" role="img" aria-label="Photo of a sphynx kitten" style="background:linear-gradient(180deg,#f4f1ee,#d7b9b1)"></div><div class="shadow"></div><a href="#">1st: Sphynx cat breeder</a></div>

  <div class="kitten" style="left:47px;top:957px"><div class="kitten-photo" role="img" aria-label="Photo of a sphynx cat" style="background:linear-gradient(135deg,#5b4332,#c9a48a)"></div><div class="shadow"></div><a href="#">1st: Sphynx cat breeder</a></div>
  <div class="kitten" style="left:193px;top:957px"><div class="kitten-photo" role="img" aria-label="Photo of two sphynx kittens" style="background:linear-gradient(135deg,#4a2e22,#b9b4be)"></div><div class="shadow"></div><a href="#">2nd: Sphynx cat</a></div>
  <div class="kitten" style="left:344px;top:957px"><div class="kitten-photo" role="img" aria-label="Photo of a grey sphynx kitten" style="background:linear-gradient(135deg,#8a7b78,#7c7f95)"></div><div class="shadow"></div><a href="#">3rd: Sphynx cat breeder</a></div>
  <div class="kitten" style="left:500px;top:957px"><div class="kitten-photo" role="img" aria-label="Photo of a sphynx cat" style="background:linear-gradient(135deg,#3a2a24,#cdb6ae)"></div><div class="shadow"></div><a href="#">4th: Sphynx cat</a></div>
  <div class="kitten" style="left:652px;top:957px"><div class="kitten-photo" role="img" aria-label="Photo of a sphynx kitten" style="background:linear-gradient(135deg,#9d9aa0,#c8b4ae)"></div><div class="shadow"></div><a href="#">2nd: Sphynx cat</a></div>
  <div class="kitten" style="left:808px;top:957px"><div class="kitten-photo" role="img" aria-label="Photo of a sphynx cat" style="background:linear-gradient(135deg,#2f2a26,#b48a70)"></div><div class="shadow"></div><a href="#">1st: Sphynx cat breeder</a></div>

  <footer class="site-footer">
    <nav class="footer-nav">
      <a href="#">Home</a><span class="sep">~</span>
      <a href="#">About Us</a><span class="sep">~</span>
      <a href="#">My breeding Cats</a><span class="sep">~</span>
      <a href="#">Kittens</a><span class="sep">~</span>
      <a href="#">Caring for a Sphynx</a><span class="sep">~</span>
      <a href="#">Contact Us</a>
    </nav>
    <p class="copyright">Copyright @ 2012 plumwickbreeders.com . All Right Reserved</p>
  </footer>
</div>
</body>
</html>
```